WordPress design project for Brindlow Construction

Brindlow Construction, Inc. (www.brindlowinc.example) is a private organization. It is run by the same family that founded Brindlow Waste Systems (www.brindlow.example), a large, publicly-held waste management organization in the US. While owned by the same family, the two organizations are run independently.
Brindlow Construction is a well-established New England USA construction outfit specializing in site development, heavy excavation, aggregate, large-scale/municipal water and sewer systems, and landfill construction and closure. Brindlow Construction is not in any way a residential or commercial building contractor.
Brindlow Construction also operates hydraulic and hydrostatic service shops, as well as aggregate (gravel, sand, stone, top soil, and anything else aggregate) sites. Both are for more traditional, non-project customers, such as landscapers and other construction companies.
Business contact information is as noted below:
Address:
Brindlow Construction, Inc.
48 Quarry Row
Fairhollow, Vermont 05799
Telephone:
802-555-0148
Fax:
802-555-0193
Email:
info@brindlowinc.example
A tagline used in a recent advertisement was:
"Committed to providing a complete array of services for over 30 years, we are New England's premier construction company."
In reviewing design ideas internally, we found bits and pieces of the following sites appealing:
TR Construction (Wendermoor) - http://www.trconstruction.example/
Halvorsk Construction - http://www.halvorsk.example/
Pellow Construction - http://www.pellowconstruction.example/
Greyfield Construction Group - http://www.greyfieldconstructiongroup.example/
Varko Construction - http://www.varko.example/
Lindqvist Brothers Construction http://www.lindqvistbros.example/
Ormsby Construction http://www.ormsby-corp.example/
The blue in the logo is hex #00253f. The logo was designed by hand many years ago, so the font is unknown.
We would like a fresh, professional design that effectively illustrates what we do in a thoughtful, impressive way.
Target Market(s)
Would-be clients, land developers, waste organizations, energy developers, engineers, surveyors, landscapers, heavy equipment operators and the likes.
Industry/Entity Type
Waste Management
Requirements
Must have
- Lots of media capabilities, such as embedded video (via YouTube is fine), project image gallery, and sliders for various functions.
A large slider on the landing page is critical, as well as space for standard things, such as news/events, job opportunities, project highlights, and the likes.
We also want to highlight things like employee longevity. Some of our team have been with us since the beginning.
We need to add emphasis to the fact that our hydraulic/hydro static services and aggregate operations are for anyone who needs such service or material. Related, we need a place to set prices and descriptions of such material to help site visitors decide what they may need.
We need a place to highlight business partners, such as Felix Harrow and Ironbeetle.
We also need form capabilities for things like bid requests and general contacts from the public. Related, there should be social media capabilities.
Nice to have
- This is almost a must have, but we're open to options. The WordPress design should be capable of fitting into the very popular PlyFrames Trellis theme.

```html
<!DOCTYPE html>
<html lang="en">
<head>
<meta charset="utf-8">
<title>Brindlow Construction</title>
<link rel="stylesheet" href="https://fonts.googleapis.com/css2?family=Arimo:wght@400;700&family=Roboto+Slab:wght@700&family=Open+Sans:wght@300;400&display=swap">
<style>
:root{
  --brand:#00253f;
  --blue:#0d3b73;
  --blue-mid:#1a4c8c;
  --ink:#333;
  --muted:#8a8a8a;
  --line:#dcdcdc;
  --band:#e9e9e9;
  --footer:#2e2e2e;
  --footer-text:#e4e4e4;
}
*{box-sizing:border-box;margin:0;padding:0}
html,body{width:799px;height:1200px;overflow:hidden}
body{position:relative;background:#fff;font-family:Arimo,Arial,sans-serif;color:var(--ink)}
.abs{position:absolute}

/* header */
.header{left:0;top:0;width:799px;height:63px;background:linear-gradient(#dfe4ea,#f3f4f6)}
.brand{left:133px;top:12px;display:flex;align-items:center;gap:8px}
.brand-mark{width:30px;height:30px;background:var(--brand)}
.brand-name{font:700 26px Arimo,Arial,sans-serif;color:var(--brand);letter-spacing:-.5px}
.social{left:597px;top:10px;display:flex;gap:4px}
.social span{width:15px;height:15px;border-radius:50%;background:var(--brand);display:block}
.search{left:516px;top:34px;width:150px;height:19px;background:#fff;border:1px solid #d4d4d4;font-size:7px;color:#bbb;padding:5px 6px}
.search svg{position:absolute;right:4px;top:3px}

/* nav */
.nav{left:0;top:63px;width:799px;height:23px;background:linear-gradient(#fff,#eee);border-top:1px solid #ddd;border-bottom:1px solid #ccc;display:flex;padding-left:134px}
.nav a{font-size:8.5px;color:#777;text-decoration:none;padding:0 14px;line-height:22px;border-right:1px solid #d6d6d6}
.nav a.active{background:var(--blue);color:#fff;padding:0 12px}

/* hero */
.hero{left:0;top:86px;width:799px;height:306px;background:linear-gradient(#c9d0d7 0%,#b7bec4 28%,#4e5a36 34%,#8c7a4a 50%,#6e5a3c 75%,#3a3430 100%)}
.arrow{top:130px}
.caption{left:232px;top:260px;width:336px;height:74px;background:rgba(24,58,110,.85);color:#fff;font:300 14.5px/17px "Open Sans",Arial,sans-serif;text-align:center;padding:10px 8px}
.hero-shadow{left:0;top:392px;width:799px;height:8px;background:radial-gradient(ellipse at top,rgba(0,0,0,.12),transparent 70%)}

/* welcome */
.welcome{left:133px;top:418px;width:341px;height:112px;border:1px solid var(--line);padding:4px 6px}
.welcome h1{font:700 20px "Roboto Slab",Georgia,serif;color:var(--blue);margin-bottom:3px}
.welcome p{font-size:5.6px;line-height:9px;color:var(--muted)}
.btn{display:inline-block;background:var(--blue);color:#fff;font-size:7px;padding:5px 6px;border:1px solid #062a55}
.welcome .btn{margin-top:5px}
.video{left:482px;top:419px;width:184px;height:112px;background:linear-gradient(#242a30,#0c0e10);box-shadow:0 1px 3px rgba(0,0,0,.4)}

/* section titles */
.sec-title{font:300 16px "Open Sans",Arial,sans-serif;color:#333;display:flex;align-items:center;gap:6px}
.sec-title::after{content:"";flex:1;border-top:1px solid var(--line)}
.pager{display:flex;gap:3px}
.pager span{width:11px;height:11px;background:var(--blue)}

/* projects */
.thumb{top:578px;width:129px;height:132px;border:3px solid #d2d2d2}

/* features band */
.band{left:0;top:742px;width:799px;height:128px;background:var(--band);border-top:2px solid var(--blue)}
.feature{top:738px;width:126px;height:128px}
.feature .tab{height:25px;background:#fff;border:1px solid #d6d6d6;font-size:8.5px;color:var(--blue);text-align:center;line-height:24px}
.feature p{font-size:5.8px;line-height:7.5px;color:var(--muted);margin-top:6px}
.feature .btn{position:absolute;right:0;top:106px}
.field{width:124px;height:17px;background:#fff;border:1px solid #ccc;margin-top:3px}
.sep{top:744px;width:1px;height:126px;background:#d4d4d4}

/* news */
.news-item{top:913px;width:126px;height:36px;border:1px solid #ddd;background:#fafafa;display:flex;gap:5px;padding:5px}
.date{width:22px;height:25px;background:#222;color:#fff;font-size:6.5px;text-align:center;line-height:10px;padding-top:2px}
.news-item h4{font-weight:400;font-size:6.5px;color:var(--blue)}
.news-item p{font-size:5.5px;color:var(--muted);line-height:7px}
.bid{left:539px;top:901px;width:127px;height:48px;border:1px solid #ddd;text-align:center;padding-top:5px}
.bid h4{font-weight:400;font-size:8.5px;color:var(--blue)}
.bid p{font-size:5.5px;color:#aaa;line-height:7px}
.bid .btn{font-size:6px;padding:2px 5px;margin-top:2px}

/* footer */
.footer{left:0;top:974px;width:799px;height:196px;background:var(--footer)}
.footer-ghost{left:135px;top:1060px;font:700 92px Arimo,Arial,sans-serif;color:#383838;letter-spacing:-3px}
.fcol{top:990px}
.fcol h3{font:400 11.5px "Open Sans",Arial,sans-serif;color:var(--footer-text);margin-bottom:17px}
.fcol li{list-style:none;font-size:6px;color:var(--footer-text);margin-bottom:9.3px}
.fcol.dots li::before{content:"";display:inline-block;width:4px;height:4px;border-radius:50%;background:#fff;margin-right:11px}
.contact p{font-size:6px;color:var(--footer-text);line-height:7.5px;margin-bottom:8px;width:100px}
.copyright{left:0;top:1170px;width:799px;height:30px;background:var(--blue);color:#7d93b3;font-size:5.5px;text-align:center;line-height:30px}
</style>
</head>
<body>

<header class="abs header"></header>
<div class="abs brand"><span class="brand-mark"></span><span class="brand-name">Brindlow</span></div>
<div class="abs social" aria-label="Social links"><span></span><span></span><span></span><span></span></div>
<div class="abs search">Search ..
  <svg width="12" height="12" viewBox="0 0 12 12"><circle cx="5" cy="5" r="3.5" fill="none" stroke="#00253f" stroke-width="1.8"/><line x1="7.5" y1="7.5" x2="11" y2="11" stroke="#00253f" stroke-width="2"/></svg>
</div>

<nav class="abs nav">
  <a class="active">Home</a><a>About Us</a><a>Services</a><a>Careers</a><a>Community &amp; Industry</a><a>Blog</a><a>Jobs</a><a style="border:0">Contact Us</a>
</nav>

<section class="abs hero" role="img" aria-label="Landfill construction site with bulldozers on graded earth under a cloudy sky"></section>
<svg class="abs arrow" style="left:105px;top:216px" width="30" height="56"><polyline points="27,2 3,28 27,54" fill="none" stroke="#fff" stroke-width="1.5"/></svg>
<svg class="abs arrow" style="left:665px;top:216px" width="30" height="56"><polyline points="3,2 27,28 3,54" fill="none" stroke="#fff" stroke-width="1.5"/></svg>
<div class="abs caption">Committed to providing a complete array of services for over 30 years, we are New England's premier construction company</div>
<div class="abs hero-shadow"></div>

<section class="abs welcome">
  <h1>Welcome!</h1>
  <p>Lorem ipsum dolor sit amet, consectetur adipiscing elit. Donec lectus velit, mattis nec scelerisque dictum nibh ac, mattis quis odio. Aenean erat mi, ornare ut lobortis semper, interdum et nulla. dictum nibh Cras iaculis, orci vel mattis facilisis, sem ipsum sagittis turpis, sit amet dictum nibh purus non ante. Fusce dictum elementum dictu est quis fermentum sagittis, mauris urna posuere orci, ac dictum nibh purus cursus risus erat interdum sem. Mauris eu dapibus neque. Lorem ipsum dolor sit amet, consectetur adipiscing elit. Curabitur bibendum purus non ante scelerisque egestas</p>
  <span class="btn">Read more</span>
</section>
<div class="abs video" role="img" aria-label="Embedded company video player">
  <svg width="184" height="112">
    <circle cx="92" cy="53" r="20" fill="#3a3f44" opacity=".8"/>
    <polygon points="86,43 86,63 102,53" fill="#ddd"/>
    <rect x="0" y="98" width="184" height="14" fill="#111"/>
    <polygon points="5,102 5,108 9,105" fill="#ccc"/>
    <rect x="13" y="104" width="96" height="2" fill="#555"/><rect x="13" y="104" width="44" height="2" fill="#d22"/>
    <text x="104" y="107.5" font-size="4.5" fill="#ccc" font-family="Arial">1:26 / 3:22</text>
    <rect x="137" y="104" width="14" height="2" fill="#d22"/>
    <text x="168" y="107.5" font-size="4.5" fill="#ccc" font-family="Arial" font-weight="bold">HD</text>
  </svg>
</div>

<div class="abs sec-title" style="left:133px;top:551px;width:500px">Projects</div>
<div class="abs pager" style="left:639px;top:557px"><span></span><span></span></div>
<div class="abs thumb" style="left:133px;background:linear-gradient(#8f9db0,#9e3a32 50%,#6a6a66)" role="img" aria-label="Red dump truck at a work site"></div>
<div class="abs thumb" style="left:268px;background:linear-gradient(#c9d6e0,#6f8a56 35%,#c7b48a 55%,#4e7c36)" role="img" aria-label="Graded hillside landfill cell beside green fields"></div>
<div class="abs thumb" style="left:402px;background:linear-gradient(#6b7580,#2f3742 50%,#8a5a44)" role="img" aria-label="Black geomembrane liner laid over earth"></div>
<div class="abs thumb" style="left:537px;background:linear-gradient(#d5d9de,#7e6d4e 45%,#4c4038)" role="img" aria-label="Bulldozer spreading debris at a landfill"></div>

<div class="abs band"></div>
<div class="abs sep" style="left:263px"></div><div class="abs sep" style="left:397px"></div><div class="abs sep" style="left:532px"></div>

<div class="abs feature" style="left:135px">
  <div class="tab">Job Opportunities</div>
  <p style="font-size:6.8px;line-height:9px">Leave us your email address and we'll send you all of the new jobs:</p>
  <p style="font-size:6.5px;color:#555">Email address:</p>
  <div class="field"></div>
  <span class="btn" style="right:-2px">Activate</span>
</div>
<div class="abs feature" style="left:270px">
  <div class="tab">Employee Longevity</div>
  <p>Lorem ipsum dolor sit amet, consectetur adipiscing elit. Sed vitae rutrum leo. Mauris id metus ut magna euismod semper. Duis at leo auctor, porta mauris sed, mattis dui. Nulla quis tellus tellus. Integer consectetur dolor dui, sed sceleris que mi elementum in. Donec vel diam tor tor.</p>
  <span class="btn">Read more</span>
</div>
<div class="abs feature" style="left:405px">
  <div class="tab">Hydraulic / Hydro</div>
  <p>Lorem ipsum dolor sit amet, consectetur adipiscing elit. Sed vitae rutrum leo. Mauris id metus ut magna euismod semper. Duis at leo auctor, porta mauris sed, mattis dui. Nulla quis tellus tellus. Integer consectetur dolor dui, sed sceleris que mi elementum in. Donec vel diam tor tor.</p>
  <span class="btn">Click here</span>
</div>
<div class="abs feature" style="left:540px">
  <div class="tab">Price of Matrial</div>
  <p><span style="color:var(--blue)">Lorem ipsum Dolor.</span><br>Lorem ipsum dolor sit amet, consectetur adipiscing elit. Sed vitae rutrum leo. Mauris id metus ut magna.</p>
  <p style="font-size:7px;color:var(--blue);margin-top:8px">Price: $1500</p>
  <span class="btn">Read more</span>
</div>

<div class="abs sec-title" style="left:133px;top:890px;width:398px">News / Events</div>
<div class="abs news-item" style="left:133px"><div class="date">July<br>5</div><div><h4>Lorem ipsum Dolor</h4><p>Consectetur adipiscing elit<br>Phasellus sed enim vesti.</p></div></div>
<div class="abs news-item" style="left:269px"><div class="date">July<br>5</div><div><h4>Lorem ipsum Dolor</h4><p>Consectetur adipiscing elit<br>Phasellus sed enim vesti.</p></div></div>
<div class="abs news-item" style="left:405px"><div class="date">July<br>5</div><div><h4>Lorem ipsum Dolor</h4><p>Consectetur adipiscing elit<br>Phasellus sed enim vesti.</p></div></div>
<div class="abs bid"><h4>Bid Requests</h4><p>Consectetur adipiscing elit<br>Phasellus sed enim.</p><span class="btn">Click here</span></div>

<footer class="abs footer"></footer>
<div class="abs footer-ghost" aria-hidden="true">Brindlow</div>
<div class="abs fcol" style="left:132px"><h3>Menu</h3><ul><li>Home</li><li>About Us</li><li>Services</li><li>Careers</li><li>Community &amp; Industry</li><li>Jobs</li><li>Contact Us</li></ul></div>
<div class="abs fcol dots" style="left:259px"><h3>Project Highlights</h3><ul><li>Lorem Ipsum Dolor</li><li>Lorem Ipsum Dolor</li><li>Lorem Ipsum Dolor</li><li>Lorem Ipsum Dolor</li></ul></div>
<div class="abs fcol dots" style="left:410px"><h3>Business Partners</h3><ul><li>Felix Harrow</li><li>Ironbeetle</li></ul></div>
<div class="abs fcol contact" style="left:568px"><h3>Contact Us</h3>
  <p>Address:<br>Brindlow Construction, Inc. 48 Quarry Row Fairhollow, Vermont 05799</p>
  <p>Telephone:<br>802-555-0148</p>
  <p>Fax:<br>802-555-0193</p>
  <p>Email:<br>info@brindlowinc.example</p>
</div>
<div class="abs copyright">© 2013 BRINDLOW, Inc. All Rights Reserved</div>

</body>
</html>
```